Brindle.vc needs a better website design!

We need a new and better website for Brindle.vc. We're a Canadian venture capital firm that invests in innovative entrepreneurs. We compete against the following websites: tollery.vc, quorbinvest.ca, gavelvc.com, and duskara.vc. We're a diverse group of partners and we're dedicated to the founders we invest in.
Updates

I don’t really like stock photos of random people as part of the website design…so please try to stay away from using those images. Thanks, Owen

Target Market(s)

Canadian entrepreneurs and investors

Industry/Entity Type

Venture capital, finance, investment, entrepreneurship

Coding

Coded - Design and coding required

Number of Pages Required

4 page

Font styles to use
Sans Serif

Colors

Designer to choose colors to be used in the design.

Requirements
Must have
• Clean crisp overall design. Fast and to the point.
Nice to have
• Check out www.brindle.vc - I did it myself and it is too basic and too wordy.
Should not have
• No stock images with random people in them! Not too wordy or with too many large images that are slow to load.

```html
<!DOCTYPE html>
<html lang="en">
<head>
<meta charset="utf-8">
<title>Brindle.vc — Venture Capital</title>
<link rel="stylesheet" href="https://fonts.googleapis.com/css2?family=Poppins:wght@400;500;600;700&display=swap">
<style>
:root{
  --green:#7a9a32;
  --green-band:#7f9c35;
  --ink:#3a3a3a;
  --muted:#555;
  --purple:#9599f5;
  --panel:#f5f6fa;
  --footer:#3e3e3e;
  --line:#dcdcdc;
}
*{margin:0;padding:0;box-sizing:border-box}
html,body{width:1200px;height:3824px;overflow:hidden;background:#fff}
body{position:relative;font-family:'Poppins',sans-serif;color:var(--ink)}
.abs{position:absolute}
.brand{display:flex;align-items:center;gap:10px;font-weight:700;color:var(--green);letter-spacing:.5px}
.brand-dot{width:38px;height:38px;border-radius:50%;border:3px solid var(--green)}
.site-logo{left:89px;top:44px;font-size:22px}
.main-nav{left:645px;top:27px;display:flex;gap:24px;font-size:12px;font-weight:600;text-transform:uppercase}
.main-nav a{color:var(--ink);text-decoration:none;padding-top:4px}
.main-nav a.active{color:var(--green);border-top:3px solid var(--green);padding-top:6px;margin-top:-5px}
.nav-cta{left:995px;top:18px;width:116px;height:35px;border:2px solid var(--ink);font-size:12px;font-weight:600;display:flex;align-items:center;justify-content:center}
.hero-photo{left:606px;top:71px;width:594px;height:666px;background:linear-gradient(180deg,#7fa7c9 0%,#d66a3a 22%,#4e6a55 40%,#2b5a35 55%,#1aa3c7 75%,#0d6f9a 100%)}
.hero-kicker{left:85px;top:288px;font-size:33px;font-weight:700;color:var(--green)}
.hero-title{left:85px;top:322px;font-size:57px;font-weight:700;line-height:58px;text-transform:uppercase;color:#3d3d3d}
.hero-text{left:89px;top:448px;font-size:15px;line-height:23px;color:var(--muted);width:480px}
.about-box{left:89px;top:738px;width:1022px;height:518px;border:2px solid var(--line);background:#fff}
.accent-frame{left:380px;top:627px;width:440px;height:220px;border:6px solid var(--green)}
.about-mark{left:552px;top:894px;width:96px;height:96px;border-radius:50%;border:4px solid var(--green)}
.about-title{left:89px;top:1012px;width:1022px;text-align:center;font-size:33px;font-weight:700;line-height:41px;text-transform:uppercase}
.about-list{left:89px;top:1102px;width:1022px;text-align:center;font-size:15px;line-height:24px;color:var(--muted)}
.member{width:222px;top:1342px}
.member .photo{height:318px;border:3px solid var(--green);background:linear-gradient(180deg,#f3f3f3 0%,#d9d5cf 60%,#3b3b3b 100%)}
.member h3{margin-top:24px;text-align:center;font-size:19px;font-weight:600;text-transform:uppercase}
.member p{text-align:center;font-size:14px;font-weight:500;color:#666;text-transform:uppercase}
.purple-band{left:0;top:1818px;width:671px;height:533px;background:var(--purple)}
.green-band{left:0;top:2351px;width:1200px;height:286px;background:var(--green-band)}
.company-shot{left:59px;top:1899px;width:513px;height:452px;background:linear-gradient(180deg,#fff38f 0%,#fff38f 70%,#fff 70%)}
.company-panel{left:572px;top:1899px;width:628px;height:533px;background:var(--panel)}
.company-kicker{left:650px;top:2092px;font-size:25px;font-weight:600;color:var(--green);text-transform:uppercase}
.company-name{left:650px;top:2118px;font-size:40px;font-weight:700;text-transform:uppercase}
.company-text{left:653px;top:2168px;width:470px;font-size:14px;line-height:22px;color:var(--muted)}
.arrow{top:2254px;width:39px;height:39px;border-radius:50%;display:flex;align-items:center;justify-content:center}
.arrow.prev{left:654px;background:#fff}
.arrow.next{left:705px;background:var(--green)}
.portfolio-title{left:88px;top:2500px;font-size:35px;font-weight:700;line-height:38px;color:#fff;text-transform:uppercase}
.btn-dark{left:927px;top:2521px;width:181px;height:42px;background:#3d3d3d;color:#fff;font-size:15px;font-weight:600;display:flex;align-items:center;justify-content:center;text-transform:uppercase}
.feature-title{font-size:35px;font-weight:700;line-height:37px;text-transform:uppercase}
.feature-text{font-size:17px;line-height:24px;color:var(--muted)}
.photo-block{background:linear-gradient(135deg,#dfe6ea,#9aa6ad 60%,#4a5a62)}
.cta-box{left:89px;top:3338px;width:1022px;height:192px;background:#fff;box-shadow:0 6px 30px rgba(0,0,0,.12);z-index:2}
.cta-title{left:138px;top:3402px;font-size:31px;font-weight:700;line-height:35px;text-transform:uppercase;z-index:3}
.btn-green{left:898px;top:3417px;width:156px;height:42px;background:var(--green);color:#fff;font-size:14px;font-weight:600;display:flex;align-items:center;justify-content:center;z-index:3}
.site-footer{left:0;top:3500px;width:1200px;height:324px;background:var(--footer)}
.footer-logo{left:0;width:1200px;top:3632px;justify-content:center;font-size:44px;gap:14px}
.footer-logo .brand-dot{width:60px;height:60px}
.footer-nav{left:0;width:1200px;top:3704px;display:flex;justify-content:center;gap:30px;font-size:15px;color:#fff;text-transform:uppercase}
.copyright{left:0;width:1200px;top:3735px;text-align:center;font-size:12px;color:#fff}
.to-top{left:1126px;top:3721px;width:48px;height:48px;border-radius:50%;background:var(--green);display:flex;align-items:center;justify-content:center}
</style>
</head>
<body>
<header>
  <div class="abs brand site-logo"><span class="brand-dot"></span>BRINDLE.VC</div>
  <nav class="abs main-nav"><a class="active">Home</a><a>Team</a><a>Companies</a><a>What we look for</a></nav>
  <div class="abs nav-cta">CONTACT US</div>
</header>

<div class="abs hero-photo" role="img" aria-label="Mountain lake landscape with sunlit peaks and evergreen forest"></div>
<div class="abs hero-kicker">BRINDLE.VC</div>
<h1 class="abs hero-title">Is a venture<br>capital firm</h1>
<p class="abs hero-text">That invests in innovative seed-stage technology companies in Western Canada focused on B2B and SaaS markets.</p>

<section>
  <div class="abs about-box"></div>
  <div class="abs accent-frame"></div>
  <div class="abs about-mark"></div>
  <h2 class="abs about-title">We are serial entrepreneurs and venture<br>capital investors who provide:</h2>
  <p class="abs about-list">Mentoring and strategic advice to help you grow your company quickly and efficiently<br>Investor introductions to help you raise additional follow-on funding for your startup</p>
</section>

<section>
  <div class="abs member" style="left:90px"><div class="photo" role="img" aria-label="Illustrated portrait of Owen Tallis"></div><h3>Owen Tallis</h3><p>Partner</p></div>
  <div class="abs member" style="left:356px"><div class="photo" role="img" aria-label="Illustrated portrait of Ravi Kandel"></div><h3>Ravi Kandel</h3><p>Partner</p></div>
  <div class="abs member" style="left:627px"><div class="photo" role="img" aria-label="Illustrated portrait of Marta Lindqvist"></div><h3>Marta Lindqvist</h3><p>Partner</p></div>
  <div class="abs member" style="left:884px"><div class="photo" role="img" aria-label="Illustrated portrait of Glenn Harrow"></div><h3>Glenn Harrow</h3><p>Advisor</p></div>
</section>

<section>
  <div class="abs purple-band"></div>
  <div class="abs green-band"></div>
  <div class="abs company-shot" role="img" aria-label="Screenshot of the Churnwise product landing page with dashboard stats"></div>
  <div class="abs company-panel"></div>
  <div class="abs company-kicker">Companies</div>
  <h2 class="abs company-name">Churnwise</h2>
  <p class="abs company-text">is a Waterloo-based, customer success AI platform for B2B SaaS companies that identifies the potential for customers to churn and helps prioritize retention efforts and increase revenues.</p>
  <div class="abs arrow prev"><svg width="10" height="10" viewBox="0 0 10 10"><path d="M6.5 2 3.5 5l3 3" fill="none" stroke="#333" stroke-width="1.4"/></svg></div>
  <div class="abs arrow next"><svg width="10" height="10" viewBox="0 0 10 10"><path d="M3.5 2 6.5 5l-3 3" fill="none" stroke="#fff" stroke-width="1.4"/></svg></div>
  <h2 class="abs portfolio-title">Check out our innovative<br>portfolio companies!</h2>
  <div class="abs btn-dark">View portfolio</div>
</section>

<section>
  <h2 class="abs feature-title" style="left:178px;top:2792px">We invest in<br>innovative</h2>
  <p class="abs feature-text" style="left:180px;top:2874px">Technology companies with<br>these characteristics:</p>
  <div class="abs photo-block" style="left:595px;top:2750px;width:427px;height:222px" role="img" aria-label="Laptop showing a bar chart on an office desk"></div>
  <div class="abs photo-block" style="left:168px;top:3003px;width:426px;height:221px" role="img" aria-label="Office team working with a tablet"></div>
  <h2 class="abs feature-title" style="left:662px;top:3045px">Other things<br>we consider</h2>
  <p class="abs feature-text" style="left:664px;top:3127px">Other things we consider in evaluating<br>our venture capital investments:</p>
</section>

<div class="abs site-footer"></div>
<div class="abs cta-box"></div>
<h2 class="abs cta-title">If you have what we're looking for,<br>contact us today.</h2>
<div class="abs btn-green">CONTACT US</div>

<footer>
  <div class="abs brand footer-logo"><span class="brand-dot"></span>BRINDLE.VC</div>
  <nav class="abs footer-nav"><span>Home</span><span>Team</span><span>Companies</span><span>What we look for</span></nav>
  <p class="abs copyright">Copyright © 2021 Brindle.vc - All Rights Reserved</p>
  <div class="abs to-top"><svg width="14" height="16" viewBox="0 0 14 16"><path d="M7 15V2M2 7l5-5 5 5" fill="none" stroke="#fff" stroke-width="1.5"/></svg></div>
</footer>
</body>
</html>
```